Divorce Lawyer print and ebook cover (Lanterns over the quiet harbor )

I need a front and back cover for my divorce and family law book. I already have a photo and title. The back cover photo is not necessary but can be interesting the Front-main cover is a must

Target Market(s)

Prospective client

Colors

Designer to choose colors to be used in the design.

Requirements
Must have
• Front photo by viewable.

```html
<!DOCTYPE html>
<html lang="en">
<head>
<meta charset="utf-8">
<title>Lanterns over the quiet harbor — cover spread</title>
<link rel="stylesheet" href="https://fonts.googleapis.com/css2?family=Alegreya+Sans:ital,wght@0,700;0,800;1,700&family=Oswald:wght@600&family=Bree+Serif&display=swap">
<style>
  :root {
    --teal: #17898a;
    --teal-deep: #0c6668;
    --teal-dark: #0a5557;
    --teal-light: #33b3ab;
    --teal-pale: #6fd0c6;
    --yellow: #f7e27a;
    --white: #ffffff;
  }
  * { margin: 0; padding: 0; box-sizing: border-box; }
  html, body { width: 1200px; height: 800px; overflow: hidden; background: var(--white); }
  .spread {
    position: relative; width: 1200px; height: 800px; overflow: hidden;
    background: var(--teal);
    font-family: "Alegreya Sans", sans-serif;
  }
  .decor { position: absolute; top: 0; height: 800px; }
  .back-decor { left: 0; width: 567px; }
  .front-decor { left: 636px; width: 564px; height: 320px; z-index: 2; }

  /* back cover */
  .back-photo {
    position: absolute; left: 243px; top: 373px; width: 300px; height: 238px;
    border-radius: 12px;
    background: linear-gradient(160deg, #b9c7c9 0%, #8f9a8f 45%, #6c6552 100%);
  }
  .back-quotes {
    position: absolute; left: 123px; top: 374px; width: 112px;
    color: var(--white); font-size: 10.5px; line-height: 1.3; font-weight: 700;
  }
  .back-quotes p + p { margin-top: 20px; }
  .back-footer {
    position: absolute; left: 40px; bottom: 24px;
    display: flex; align-items: center; gap: 18px;
    color: var(--white); font-size: 10.5px; font-weight: 700;
  }
  .imprint { display: flex; align-items: center; gap: 6px; font-size: 11px; }
  .imprint-dot { width: 18px; height: 18px; border-radius: 50%; background: var(--white); }
  .contact { display: flex; align-items: center; gap: 6px; }
  .contact svg { width: 14px; height: 14px; }

  /* spine */
  .spine {
    position: absolute; left: 567px; top: 0; width: 69px; height: 800px;
    background: var(--teal-deep);
  }
  .spine-text {
    position: absolute; left: 50%; white-space: nowrap;
    transform: translate(-50%, -50%) rotate(-90deg);
  }
  .spine-author { top: 68px; color: var(--white); font-size: 15px; font-weight: 700; }
  .spine-title {
    top: 445px; font-family: "Oswald", sans-serif; font-weight: 600;
    font-size: 33px; letter-spacing: 0.5px; color: var(--white);
  }
  .spine-title .join { font-family: "Alegreya Sans", sans-serif; font-style: italic; font-size: 20px; color: var(--yellow); margin: 0 8px; }
  .spine-title .accent { color: var(--yellow); }

  /* front cover */
  .front-photo {
    position: absolute; left: 636px; top: 0; width: 564px; height: 740px;
    background:
      radial-gradient(ellipse at 80% 45%, rgba(240,226,120,0.85) 0%, rgba(240,226,120,0) 55%),
      linear-gradient(180deg, #9aa7ad 0%, #7d8a8f 55%, #3c4448 100%);
  }
  .front-title {
    position: absolute; right: 60px; top: 52px; z-index: 3;
    text-align: right; font-weight: 800; line-height: 1;
  }
  .front-title .line-top { display: block; color: var(--white); font-size: 38px; letter-spacing: 0.5px; }
  .front-title .join { display: block; color: var(--yellow); font-style: italic; font-weight: 700; font-size: 21px; margin: 6px 80px 6px 0; }
  .front-title .line-main { display: block; color: var(--yellow); font-size: 43px; letter-spacing: 0.5px; }
  .front-band {
    position: absolute; left: 636px; top: 740px; width: 564px; height: 60px;
    background: var(--teal);
  }
  .front-author {
    position: absolute; right: 48px; bottom: 56px; z-index: 3;
    font-family: "Bree Serif", serif; font-size: 30px; line-height: 1; color: var(--teal);
  }
</style>
</head>
<body>
<main class="spread">
  <svg class="decor back-decor" viewBox="0 0 567 800" aria-hidden="true">
    <rect x="0" y="0" width="567" height="800" fill="var(--teal)"/>
    <path d="M0 0 H567 V330 C470 260 380 200 260 160 C160 130 70 140 0 150 Z" fill="var(--teal-deep)"/>
    <path d="M0 150 C70 140 160 130 260 160 C380 200 470 260 567 330 V350 C470 285 380 222 260 184 C160 156 70 164 0 176 Z" fill="var(--teal-pale)" opacity="0.7"/>
    <path d="M0 0 H230 C190 40 150 70 0 100 Z" fill="var(--teal-light)" opacity="0.5"/>
    <path d="M0 230 C60 250 90 330 60 420 C40 480 20 520 0 540 Z" fill="var(--teal-dark)" opacity="0.8"/>
    <path d="M0 210 C70 232 110 330 76 430 C56 490 28 530 0 556 V540 C20 520 40 480 60 420 C90 330 60 250 0 230 Z" fill="var(--teal-pale)" opacity="0.55"/>
    <g stroke="var(--white)" stroke-width="2" opacity="0.35">
      <line x1="120" y1="40" x2="290" y2="180"/>
      <line x1="145" y1="30" x2="300" y2="160"/>
      <line x1="170" y1="20" x2="310" y2="140"/>
      <line x1="195" y1="10" x2="320" y2="118"/>
    </g>
  </svg>

  <!-- back cover -->
  <section class="back-cover">
    <div class="back-quotes">
      <p>"Lorem ipsum dolor sit amet, consectetur adipiscing elit, sed do eiusmod tempor incididunt ut labore et dolore magna aliqua. Ut enim ad minim veniam"</p>
      <p>"Lorem ipsum dolor sit amet, consectetur adipiscing elit"</p>
    </div>
    <div class="back-photo" role="img" aria-label="Photo of a small child in a knitted hat sitting on a park swing, held by two adults"></div>
    <footer class="back-footer">
      <span class="imprint"><span class="imprint-dot"></span>Harborline</span>
      <span class="contact">
        <svg viewBox="0 0 14 14" aria-hidden="true"><circle cx="7" cy="7" r="6" fill="none" stroke="#fff" stroke-width="1.2"/><path d="M4.5 4 L6 4 L6.5 5.5 L5.7 6.2 C6.2 7.2 6.8 7.8 7.8 8.3 L8.5 7.5 L10 8 L10 9.5 C7 9.8 4.2 7 4.5 4 Z" fill="#fff"/></svg>
        001 555 0142
      </span>
      <span class="contact">
        <svg viewBox="0 0 14 14" aria-hidden="true"><circle cx="7" cy="7" r="6" fill="none" stroke="#fff" stroke-width="1.2"/><rect x="3.8" y="4.8" width="6.4" height="4.4" fill="none" stroke="#fff" stroke-width="1"/><path d="M3.8 4.8 L7 7.4 L10.2 4.8" fill="none" stroke="#fff" stroke-width="1"/></svg>
        Your e-mail here
      </span>
    </footer>
  </section>

  <!-- spine -->
  <section class="spine">
    <span class="spine-text spine-author">Author's name</span>
    <span class="spine-text spine-title">LANTERNS OVER<span class="join">the</span><span class="accent">QUIET HARBOR</span></span>
  </section>

  <!-- front cover -->
  <section class="front-cover">
    <div class="front-photo" role="img" aria-label="Photo of a man in a suit standing at a fork in a misty park road before a signpost pointing to Old Life and New Life"></div>
    <svg class="decor front-decor" viewBox="0 0 564 320" aria-hidden="true">
      <path d="M0 0 H564 V187 C484 200 420 285 324 285 C224 285 124 120 0 113 Z" fill="var(--teal)"/>
      <path d="M0 113 C124 120 224 285 324 285 C420 285 484 200 564 187 V203 C486 216 424 301 324 301 C220 301 120 136 0 129 Z" fill="var(--teal-light)"/>
      <g stroke="var(--white)" stroke-width="2" opacity="0.3">
        <line x1="350" y1="270" x2="564" y2="150"/>
        <line x1="372" y1="276" x2="564" y2="168"/>
        <line x1="330" y1="262" x2="564" y2="132"/>
      </g>
    </svg>
    <div class="front-band"></div>
    <h1 class="front-title">
      <span class="line-top">LANTERNS OVER</span>
      <span class="join">the</span>
      <span class="line-main">QUIET HARBOR</span>
    </h1>
    <p class="front-author">Author's name</p>
  </section>
</main>
</body>
</html>
```